Rogue Beneath Ash - YA Book Cover Design

Front and Back and Spine Required
Print Ready File Please
Our publishing company needs a book cover design ready to go by November 20th. Primary colour scheme is yellow/orange/bronze. The book is aimed at a YA audience and follows themes of espionage and thieves.
**I really want the cover to have a fun-mischievous and adventure appeal to it.**

The main character had brown hair and purple eyes, if that makes a difference to your design. It is the third book in the series, for the other books please look at www.plmarrow.co.uk . Feedback from those books were that they were too dark and the author isn't a big fan. She thinks it's a little bland. We're really hoping that whoever wins this project will have space in the future to re-design the original two. That being said, it will be in the future so needs the new design needs to fit in with the current work. Other than that we're interested in designers having some creative freedom to produce what they think is best for the series.

Also please include the RWL logo on the spine (will be uploaded) and the Omicron Vale symbol on the back page (also uploaded). Page size if 5" by 8" and the page count is roughly 315. Be open to potentially changing that slightly but it shouldn't be by much. I look forward to seeing your designs.

BLURB:When her Mum suggested a holiday in Barcelona, the last thing Liv expected was to return without her father. With Howard kidnapped and sporting injuries of her own, Liv must try her best to work within the law to find him instead of returning to her illegal roots. But it would seem fate has other ideas, forcing her back to the Underground at every turn. Can Liv find her father before it's too late?Who took him and why?And who is the mysterious boy that saved her from the same fate?

Target Market(s)

YA and Teen - Girls ages 14-22

Font styles to use
Serif
Sans Serif
Decorative
Script

Colors

Designer to choose colors to be used in the design.

Requirements
Must have
• Also please include the RWL logo on the spine (will be uploaded) between title and author name. Also include the Omicron Vale symbol on the back page (also uploaded). Page size if 5" by 8" and the page count is roughly 315. Be open to potentially changing that slightly but it shouldn't be by much.
• Must fit in with series - see www.plmarrow.co.uk for other covers
Nice to have
• Primary colour scheme is yellow/orange/bronze. The book is aimed at a YA audience and follows themes of espionage and thieves. I really want the cover to have a fun-mischievous and adventure appeal to it. The main character had brown hair and purple eyes, if that makes a difference to your design. Although in the other books in the series we have characters back facing or partially facing.
• It is the third book in the series, for the other books please look at www.plmarrow.co.uk .
• Needs to fit in with the other books in the series. Other than that we're interested in designers having some creative freedom to produce what they think is best for the series.
Should not have
• Unable to be printed
• Not fit in with other books in series
• Only e-book format

```html
<!DOCTYPE html>
<html lang="en">
<head>
<meta charset="utf-8">
<title>Rogue Beneath Ash – Cover Spread</title>
<link rel="stylesheet" href="https://fonts.googleapis.com/css2?family=Cinzel:wght@400;600&display=swap">
<style>
  :root {
    --page: #ffffff;
    --stone: #141313;
    --stone-light: #34312f;
    --stone-warm: #2a2420;
    --gold: #e2bd1e;
    --amber: #e8861c;
    --bronze: #b8682a;
    --ink-light: #f4f4f4;
    --flame-yellow: #f7c11e;
    --flame: #ef7a14;
    --flame-deep: #8a3208;
    --iris: #8b2fb8;
    --spine-mark: #e5788a;
  }
  * { margin: 0; padding: 0; box-sizing: border-box; }
  html, body { width: 1200px; height: 1200px; overflow: hidden; background: var(--page); }
  .canvas { position: relative; width: 1200px; height: 1200px; }

  .spread {
    position: absolute; left: 22px; top: 181px; width: 1156px; height: 869px;
    background:
      radial-gradient(circle at 12% 18%, var(--stone-light), transparent 22%),
      radial-gradient(circle at 38% 62%, var(--stone-light), transparent 20%),
      radial-gradient(circle at 58% 20%, var(--stone-warm), transparent 24%),
      radial-gradient(circle at 22% 88%, var(--stone-light), transparent 18%),
      radial-gradient(circle at 92% 12%, var(--stone-light), transparent 20%),
      radial-gradient(circle at 94% 90%, var(--stone-warm), transparent 22%),
      var(--stone);
    overflow: hidden;
  }

  .title-word, .title-line {
    font-family: "Cinzel", serif;
    background: linear-gradient(90deg, var(--gold), var(--amber) 55%, var(--bronze));
    -webkit-background-clip: text; background-clip: text; color: transparent;
    white-space: nowrap; line-height: 1;
  }

  /* Back cover */
  .back-title { position: absolute; left: 56px; width: 450px; top: 72px; text-align: center; }
  .back-title .title-word { font-size: 62px; display: block; }
  .back-title .title-line { font-size: 34px; display: block; margin-top: 4px; }

  .blurb {
    position: absolute; left: 55px; top: 272px; width: 418px;
    font-family: "Cinzel", serif; font-size: 15.6px; line-height: 21px;
    color: var(--ink-light); text-align: justify; text-transform: uppercase;
    letter-spacing: 0.3px;
  }

  .imprint-name {
    position: absolute; left: 56px; top: 760px;
    font-family: "Cinzel", serif; font-size: 20px; font-weight: 600;
    color: var(--bronze); display: flex; align-items: center; gap: 10px;
  }
  .imprint-name .mark { width: 22px; height: 22px; background: var(--bronze); }

  .code-box { position: absolute; left: 304px; top: 704px; width: 210px; height: 127px; background: #ffffff; }

  /* Spine */
  .spine-title {
    position: absolute; left: 578px; top: 95px;
    transform-origin: left top; transform: translateX(50px) rotate(90deg);
  }
  .spine-title .title-word { font-size: 34px; display: block; }
  .spine-title .title-line { font-size: 22px; display: block; }

  .spine-publisher {
    position: absolute; left: 578px; top: 424px; width: 44px; text-align: center;
    font-family: "Cinzel", serif; font-size: 13px; font-weight: 600; color: var(--spine-mark);
  }

  .spine-author {
    position: absolute; left: 590px; top: 640px;
    transform-origin: left top; transform: translateX(28px) rotate(90deg);
    font-family: "Cinzel", serif; font-size: 30px; color: var(--ink-light); white-space: nowrap;
  }

  /* Front cover */
  .cover-art {
    position: absolute; left: 650px; top: 123px; width: 424px; height: 680px;
    background:
      radial-gradient(ellipse 28% 14% at 50% 42%, var(--iris) 0%, rgba(139,47,184,0.5) 55%, transparent 100%),
      radial-gradient(ellipse 50% 50% at 50% 50%, var(--flame-deep) 0%, var(--flame) 40%, rgba(247,193,30,0.75) 62%, rgba(239,122,20,0.25) 80%, transparent 100%);
  }

  .front-title { position: absolute; left: 660px; width: 490px; top: 44px; text-align: center; }
  .front-title .title-word { font-size: 108px; display: block; }
  .front-title .title-line { font-size: 52px; display: block; margin-top: 10px; }

  .front-author {
    position: absolute; left: 660px; width: 490px; top: 808px; text-align: center;
    font-family: "Cinzel", serif; font-size: 40px; color: var(--ink-light); line-height: 1;
  }
</style>
</head>
<body>
<div class="canvas">
  <section class="spread">
    <!-- Back cover -->
    <div class="back-title">
      <span class="title-word">ROGUE</span>
      <span class="title-line">BENEATH ASH</span>
    </div>
    <p class="blurb">When her Mum suggested a holiday in Barcelona, the last thing Liv expected was to return without her father. With Howard kidnapped and sporting injuries of her own, Liv must try her best to work within the law to find him instead of returning to her illegal roots. But it would seem fate has other ideas, forcing her back to the Underground at every turn. Can Liv find her father before it's too late? Who took him and why? And who is the mysterious boy that saved her from the same fate?</p>
    <div class="imprint-name"><span class="mark"></span>Omicron Vale</div>
    <div class="code-box"></div>

    <!-- Spine -->
    <div class="spine-title">
      <span class="title-word">ROGUE</span>
      <span class="title-line">BENEATH ASH</span>
    </div>
    <div class="spine-publisher">RWL</div>
    <div class="spine-author">P.L.MARROW</div>

    <!-- Front cover -->
    <div class="cover-art" role="img" aria-label="Purple eye peering through a keyhole ringed by bright orange and yellow flames"></div>
    <div class="front-title">
      <span class="title-word">ROGUE</span>
      <span class="title-line">BENEATH ASH</span>
    </div>
    <div class="front-author">P.L.MARROW</div>
  </section>
</div>
</body>
</html>
```